Letterhead for a Natural Hair Run

We need a letterhead design with the logo uploaded entitled 'Bluevista Dash'. This run is a natural 5K run seeking to promote the acceptance of natural beauty in every aspect of society encompassing one's ethnic roots and its connection to a healthy lifetstyle. We would like to see designs coordinating with our logo. The design should be fun and exciting!

Industry/Entity Type

Hair

Font styles to use
Serif
Sans Serif

Requirements
Must have
• Please included this information on the letter head:
• P.O. Box K7214
• Nassau, Bahamas
• Phone: (242) 618-2097
• Email: goskyward517@mailbrisk.net

```html
<!DOCTYPE html>
<html lang="en">
<head>
<meta charset="utf-8">
<title>Bluevista Dash Letterhead</title>
<link rel="stylesheet" href="https://fonts.googleapis.com/css2?family=Arimo:wght@400&display=swap">
<style>
  :root {
    --canvas: #ffffff;
    --paper: #ffffff;
    --paper-edge: #8a8a8a;
    --sun-yellow: #fbd915;
    --sky-blue: #7fd6e6;
    --ink-grey: #5f5f5f;
    --ink-dark: #1a1a1a;
    --figure-tone: #2a2a2a;
  }
  * { margin: 0; padding: 0; box-sizing: border-box; }
  html, body {
    width: 1000px;
    height: 1200px;
    overflow: hidden;
    background: var(--canvas);
  }
  .letterhead {
    position: absolute;
    left: 189px;
    top: 158px;
    width: 606px;
    height: 912px;
    background: var(--paper);
    border: 1px solid var(--paper-edge);
    box-shadow: 2px 3px 4px rgba(0, 0, 0, 0.12);
    overflow: hidden;
  }
  .brand {
    position: absolute;
    left: 26px;
    top: 14px;
    width: 150px;
  }
  .brand-figures {
    width: 144px;
    height: 74px;
    background: var(--figure-tone);
  }
  .brand-name {
    margin-top: 3px;
    font-family: "Arimo", Arial, sans-serif;
    font-size: 15px;
    line-height: 18px;
    font-weight: 400;
    color: var(--ink-dark);
    white-space: nowrap;
  }
  .contact {
    position: absolute;
    right: 31px;
    top: 27px;
    font-family: "Arimo", Arial, sans-serif;
    font-size: 10px;
    line-height: 14px;
    color: var(--ink-grey);
    text-align: right;
    font-style: normal;
  }
  .waves {
    position: absolute;
    left: 0;
    top: 0;
    width: 606px;
    height: 200px;
  }
  .wave-blue { fill: var(--sky-blue); }
  .wave-yellow { fill: var(--sun-yellow); }
  .footer-band {
    position: absolute;
    left: 0;
    bottom: 0;
    width: 100%;
    height: 15px;
    background: var(--sun-yellow);
  }
</style>
</head>
<body>
  <main class="letterhead">
    <svg class="waves" viewBox="0 0 606 200" aria-hidden="true">
      <path class="wave-blue" d="M0,147 C100,120 250,122 340,133 C460,140 560,110 606,64 L606,97 C540,135 430,140 340,135 C230,128 100,140 0,175 Z"/>
      <path class="wave-yellow" d="M0,127 C120,105 250,110 340,125 C450,142 540,140 606,114 L606,152 C540,172 440,168 340,148 C240,128 120,120 0,139 Z"/>
    </svg>

    <header class="brand">
      <div class="brand-figures" role="img" aria-label="Silhouettes of a family running together"></div>
      <div class="brand-name">Bluevista Dash</div>
    </header>

    <address class="contact">
      <div>P.O. Box K7214</div>
      <div>Nassau, Bahamas</div>
      <div>Phone: (242) 618-2097</div>
      <div>Email: goskyward517@mailbrisk.net</div>
    </address>

    <div class="footer-band"></div>
  </main>
</body>
</html>
```